Wordpress website for a new Podcast

Hi, We are looking for a designer to create a wordpress website project for a new podcast and publish it on the domain we own.

The show is called “Bright Gatherings” (logo included) and its aim is to interview guests who work as professional facilitators, trainers, teachers and coaches. The show has a positive vibe, is fun, vibrant and full of positive energy. These are the feelings we want to convey in the design.

The website should have a similar structure to: https://www.corefocusloop.example/ with the following content:

1) The main page including:
- navigation bar and social buttons at the top
- main graphic design featuring the latest episode
- "latest episodes" section displaying 3 episodes (please design a mask to be used for new episodes when they air together with the face of the interviewee) -> this will link to the respective episodes
- please design an "bright gatherings" book cover mockup to be inluded as a banner -> this will link to Bookvale
- subscribe to the newsletter - a banner capturing the name and email of the user -> to be connected to PostFinch.
-> a working episode search.

2) Episodes page
- the show will be divided into seasons (12 episodes each) and each episode will need a separate "blog entry" including:
-> A short article (4-5 paragraphs) + stock image
-> interviewee's bio and social links

3) Meet the hosts page
- including bios of the two hosts of the show
- links to their social profiles
- a "request speaker availability" form which sends an email

Some additional nice-to-haves:
1) Good and clean Bio's would be awesome (both for the hosts & the interviewees),
2) an easily navigable episode system,
3) a keyword/date search option
4) easy to share options (share to ChatNest, Friendlane, Chirpline, CareerMesh) 5) We must be able to track how the podcasts are shared (trackwise metrics?)

```html
<!DOCTYPE html>
<html lang="en">
<head>
<meta charset="utf-8">
<title>Bright Gatherings</title>
<link rel="stylesheet" href="https://fonts.googleapis.com/css2?family=Josefin+Sans:wght@400;600;700&family=Lato:wght@400;700&family=Open+Sans:wght@400;600&display=swap">
<style>
:root{
  --orange:#e9450f;
  --orange-2:#f5740c;
  --yellow:#edbe18;
  --ink:#1c1c1c;
  --dark:#232323;
  --muted:#555;
  --line:#bdbdbd;
  --white:#fff;
}
*{margin:0;padding:0;box-sizing:border-box}
a{text-decoration:none}
html,body{width:1200px;height:2653px;overflow:hidden;background:var(--white)}
body{position:relative;font-family:"Lato",sans-serif;color:var(--ink)}
.head{font-family:"Josefin Sans",sans-serif;font-weight:700}

/* header */
.site-header{position:absolute;left:0;top:0;width:1200px;height:97px;background:var(--white);z-index:3}
.brand{position:absolute;left:108px;top:16px;width:166px;height:166px;border-radius:50%;background:var(--white);border:2px solid #dcdcdc;display:flex;align-items:center;justify-content:center;text-align:center;z-index:4}
.brand span{font-family:"Josefin Sans",sans-serif;font-weight:700;font-size:21px;line-height:1.15;color:var(--orange)}
.nav{position:absolute;top:42px;left:351px;display:flex;gap:29px;font-family:"Josefin Sans",sans-serif;font-weight:600;font-size:16px}
.nav a{color:var(--ink)}
.nav a.active{color:var(--orange-2)}
.search{position:absolute;left:699px;top:28px;width:249px;height:41px;border:1px solid #9a9a9a;display:flex;align-items:center;padding-left:14px;gap:8px;font-family:"Josefin Sans",sans-serif;font-size:17px;color:#777}
.social-top{position:absolute;left:960px;top:34px;width:138px;display:grid;grid-template-columns:1fr 1fr;gap:3px 6px;font-size:11px;font-weight:700;color:var(--ink)}

/* hero */
.hero{position:absolute;left:0;top:97px;width:1200px;height:585px;background:linear-gradient(180deg,#151515 0%,#3a3a3a 45%,#7d7d7d 80%,#9a9a9a 100%)}
.hero-title{position:absolute;left:111px;top:288px;font-size:64px;color:var(--white);letter-spacing:1px}
.hero-text{position:absolute;left:111px;top:380px;width:560px;font-family:"Open Sans",sans-serif;font-size:22px;line-height:39px;color:var(--white)}
.btn{display:flex;align-items:center;justify-content:center;font-family:"Josefin Sans",sans-serif;font-weight:700;border-radius:40px;text-transform:uppercase}
.btn-solid{background:var(--yellow);color:var(--white)}
.hero-btn{position:absolute;left:111px;top:491px;width:195px;height:61px;font-size:18px}
.dots{position:absolute;left:564px;top:584px;display:flex;gap:6px}
.dots i{width:13px;height:13px;border-radius:50%;border:2px solid var(--white)}
.dots i.on{background:var(--white)}

/* episodes */
.section-title{position:absolute;left:0;width:1200px;text-align:center}
.episodes-title{top:772px;font-size:46px}
.card{position:absolute;top:871px;width:311px;height:526px;border:1px solid var(--line);text-align:center}
.card-photo{height:225px;background:linear-gradient(135deg,#7a6a5a,#c49a6c 55%,#4a3a30)}
.card-icon{position:absolute;left:128px;top:198px;width:55px;height:55px}
.ep-num{margin-top:44px;font-family:"Josefin Sans",sans-serif;font-size:18px;color:#444}
.ep-title{margin-top:12px;font-family:"Josefin Sans",sans-serif;font-weight:600;font-size:25px}
.ep-text{margin:18px auto 0;width:250px;font-size:15.5px;line-height:28px;color:#444}
.btn-outline{margin:22px auto 0;width:139px;height:48px;border:2px solid var(--yellow);color:var(--yellow);font-size:16px}

/* book */
.book-band{position:absolute;left:0;top:1511px;width:1200px;height:507px;background:linear-gradient(120deg,#262626,#1d1d1d 60%,#2a2a2a);overflow:hidden}
.book-ring{position:absolute;left:15px;top:-27px;width:561px;height:561px;border-radius:50%;background:#1a1a1a}
.book-disc{position:absolute;left:38px;top:-3px;width:514px;height:514px;border-radius:50%;background:var(--white)}
.book-cover{position:absolute;left:153px;top:56px;width:275px;height:385px;background:linear-gradient(160deg,var(--orange),var(--orange-2) 55%,var(--yellow));border:3px solid #111}
.book-title{position:absolute;left:647px;top:130px;font-size:45px;color:var(--white)}
.book-text{position:absolute;left:647px;top:215px;width:440px;font-size:18px;line-height:37px;color:#e8e8e8}
.book-btn{position:absolute;left:647px;top:329px;width:238px;height:62px;font-size:18px}
.store{position:absolute;left:926px;top:344px;font-family:"Josefin Sans",sans-serif;font-weight:700;font-size:30px;color:var(--white)}

/* newsletter */
.newsletter{position:absolute;left:0;top:2018px;width:1200px;height:313px;background:var(--orange)}
.news-title{top:62px;font-size:47px;color:var(--white)}
.news-text{top:138px;font-size:17px;color:var(--white)}
.field{position:absolute;top:191px;width:297px;height:50px;background:var(--white);padding-left:14px;display:flex;align-items:center;font-size:17px;color:#444}
.news-btn{position:absolute;left:838px;top:185px;width:160px;height:61px;font-size:19px}

/* footer */
.foot-social{position:absolute;left:0;top:2427px;width:1200px;display:flex;justify-content:center;gap:10px}
.foot-social span{height:48px;padding:0 14px;border:1.5px solid var(--yellow);border-radius:24px;display:flex;align-items:center;font-size:13px;font-weight:700;color:var(--yellow)}
.contact{position:absolute;left:0;top:2507px;width:1200px;text-align:center;font-family:"Josefin Sans",sans-serif;font-size:15.5px;color:#444}
.contact b{color:var(--yellow);font-weight:400;margin:0 8px}
.links{top:2548px}
.copy{top:2589px}
</style>
</head>
<body>

<header class="site-header">
  <nav class="nav">
    <a class="active" href="#">HOME</a>
    <a href="#">EPISODES</a>
    <a href="#">MEET THE HOSTS</a>
  </nav>
  <div class="search">
    <svg width="15" height="15" viewBox="0 0 16 16"><circle cx="6.5" cy="6.5" r="5" fill="none" stroke="#333" stroke-width="2"/><path d="M10.3 10.3L15 15" stroke="#333" stroke-width="2"/></svg>
    Search
  </div>
  <div class="social-top">
    <span>Friendlane</span><span>Chirpline</span>
    <span>CareerMesh</span><span>ChatNest</span>
  </div>
</header>
<a class="brand" href="#"><span>Bright<br>Gatherings</span></a>

<section class="hero" role="img" aria-label="Black and white photo of a large audience seated in a lecture hall"></section>
<h1 class="head hero-title">BRIGHT GATHERINGS</h1>
<p class="hero-text">Aim is to interview guests who work as professional facilitators, trainers, teachers and coaches</p>
<a class="btn btn-solid hero-btn" href="#">Explore now!</a>
<div class="dots"><i class="on"></i><i></i><i></i><i></i></div>

<h2 class="head section-title episodes-title">LATEST EPISODES</h2>

<article class="card" style="left:110px">
  <div class="card-photo" role="img" aria-label="Photo of women in an audience listening attentively"></div>
  <svg class="card-icon" viewBox="0 0 55 55"><circle cx="27.5" cy="27.5" r="27.5" fill="#e9450f"/><circle cx="27.5" cy="25" r="14" fill="none" stroke="#fff" stroke-width="2.5"/><circle cx="27.5" cy="25" r="8.5" fill="none" stroke="#fff" stroke-width="2.5"/><circle cx="27.5" cy="25" r="3.2" fill="#fff"/><path d="M25 30h5l-1 13h-3z" fill="#fff"/></svg>
  <div class="ep-num">Episode 200</div>
  <h3 class="ep-title">Finibus Bonoret Malorum</h3>
  <p class="ep-text">Neque porro quisquam est, qui dolorem ipsum quia dolor sit amet, consectetur, adipisci velit</p>
  <a class="btn btn-outline" href="#">Listen now!</a>
</article>

<article class="card" style="left:445px">
  <div class="card-photo" role="img" aria-label="Photo of a speaker with a headset facing a seated audience" style="background:linear-gradient(135deg,#2a2a2a,#8a6a4a 55%,#c8a27a)"></div>
  <svg class="card-icon" viewBox="0 0 55 55"><circle cx="27.5" cy="27.5" r="27.5" fill="#e9450f"/><circle cx="27.5" cy="25" r="14" fill="none" stroke="#fff" stroke-width="2.5"/><circle cx="27.5" cy="25" r="8.5" fill="none" stroke="#fff" stroke-width="2.5"/><circle cx="27.5" cy="25" r="3.2" fill="#fff"/><path d="M25 30h5l-1 13h-3z" fill="#fff"/></svg>
  <div class="ep-num">Episode 199</div>
  <h3 class="ep-title">Finibus Bonoret Malorum</h3>
  <p class="ep-text">Neque porro quisquam est, qui dolorem ipsum quia dolor sit amet, consectetur, adipisci velit</p>
  <a class="btn btn-outline" href="#">Listen now!</a>
</article>

<article class="card" style="left:779px">
  <div class="card-photo" role="img" aria-label="Photo of a presenter gesturing in front of a projected slide" style="background:linear-gradient(135deg,#b5623a,#cfe3ea 45%,#3a2c26)"></div>
  <svg class="card-icon" viewBox="0 0 55 55"><circle cx="27.5" cy="27.5" r="27.5" fill="#e9450f"/><circle cx="27.5" cy="25" r="14" fill="none" stroke="#fff" stroke-width="2.5"/><circle cx="27.5" cy="25" r="8.5" fill="none" stroke="#fff" stroke-width="2.5"/><circle cx="27.5" cy="25" r="3.2" fill="#fff"/><path d="M25 30h5l-1 13h-3z" fill="#fff"/></svg>
  <div class="ep-num">Episode 198</div>
  <h3 class="ep-title">Finibus Bonoret Malorum</h3>
  <p class="ep-text">Neque porro quisquam est, qui dolorem ipsum quia dolor sit amet, consectetur, adipisci velit</p>
  <a class="btn btn-outline" href="#">Listen now!</a>
</article>

<section class="book-band">
  <div class="book-ring"></div>
  <div class="book-disc"></div>
  <div class="book-cover" role="img" aria-label="Hardcover book mockup with an orange cover"></div>
  <h2 class="head book-title">BRIGHT GATHERINGS</h2>
  <p class="book-text">Ut enim ad minima veniam, quis nostrum exer ullam corporis suscipit laboriosam, nisi ut aliq..</p>
  <a class="btn btn-solid book-btn" href="#">Get the book now</a>
  <span class="store">Bookvale</span>
</section>

<section class="newsletter">
  <h2 class="head section-title news-title">NEWSLETTER SUBSCRIPTION</h2>
  <p class="section-title news-text">Nemo enim ipsam voluptatem quia voluptas sit aspernatur aut</p>
  <div class="field" style="left:202px">Name</div>
  <div class="field" style="left:516px">Email</div>
  <a class="btn btn-solid news-btn" href="#">Subscribe</a>
</section>

<footer>
  <div class="foot-social"><span>Friendlane</span><span>Chirpline</span><span>CareerMesh</span><span>ChatNest</span></div>
  <p class="contact">
    <svg width="10" height="14" viewBox="0 0 10 14"><path d="M5 0a5 5 0 0 0-5 5c0 4 5 9 5 9s5-5 5-9a5 5 0 0 0-5-5zm0 7a2 2 0 1 1 0-4 2 2 0 0 1 0 4z" fill="#edbe18"/></svg>
    418 Lantern Road, Suite 52 Maplebrook, NY 10990 <b>|</b>
    <svg width="12" height="12" viewBox="0 0 12 12"><path d="M2.5 0l2 3-1.2 1.5a7 7 0 0 0 4.2 4.2L9 7.5l3 2-1.5 2.5C5 12 0 7 0 1.5z" fill="#edbe18"/></svg>
    1 555 014 2207 <b>|</b>
    <svg width="15" height="11" viewBox="0 0 15 11"><rect width="15" height="11" rx="1" fill="#edbe18"/><path d="M0 1l7.5 5L15 1" fill="none" stroke="#fff" stroke-width="1.3"/></svg>
    hello@brightgatherings.example
  </p>
  <p class="contact links">Help <b>|</b> FAQ <b>|</b> Support <b>|</b> Sitemap <b>|</b> Terms Of Use <b>|</b> Privacy Statement</p>
  <p class="contact copy">Bright Gatherings © 2019 All rights reserved.</p>
</footer>

</body>
</html>
```